Signage Design job – Healthcare IT Company Needs a Core Values Poster for Office

We want to make a poster for our offices that beautifully presents our core values.

We want the design to be fun, young and colourful while showing some sophistication.

The poster will be visible to the staff (within the open plan office), and the right colours will need to be used to enhance mood and productivity. Perhaps we could be looking at a colour for each core value? Or potentially some other way for each value to stand out? We have other culture posters that have been created in the past that we would like to stay similar to in style for cohesiveness.

Our office walls are primarily white and navy blue with accents of orange, grey, and turquoise.

In terms of size - we aren't 100% on what size we want, but not only will be print it on the walls, we will also be printing out mini versions for people to put in their cubicles so keep that in mind for font legibility.

Fonts can be experimented with, but they main body font should be Source Sans Pro.

It needs to be clear, punchy and stand out from across the office (while being easy on the eye)

We have a series of cartoon guardians that can be incorporated into the design as well.

I have attached a few sample images that can be used as inspiration. We would like more colour throughout the design. 

Final file should be AI or EPS vector file.

Target Market(s)

Internal employees age range from 25-60

Font styles to use
Sans Serif
Other font styles liked:
• Please use Source Sans Pro

Colors
abd037
6b449b
33a6d7
f37122
0355a3
ffcf3e
e34297

Requirements
Must have
• Must use our colors. Must feel fresh and energetic. Must emphasize important key words. Must feel inspirational. Must align with our internal branding. Look at the 4 posters I have included in the files to understand our look. Our company website is www.kelvantis.com
Nice to have
• Mission Statement is not necessary if there isn't enough room on the poster.
Should not have
• Should not be cluttered looking in such a way that you can't get the message.

```html
<!DOCTYPE html>
<html lang="en">
<head>
<meta charset="utf-8">
<title>Kelvantis – Core Values</title>
<link rel="stylesheet" href="https://fonts.googleapis.com/css2?family=Montserrat:wght@500;600;700;800&family=Source+Sans+3:wght@400;600;700&display=swap">
<style>
  :root{
    --navy:#1d2f5e;
    --orange:#f15a22;
    --orange-soft:#f37122;
    --ink:#2b2b2b;
    --muted:#8a8f99;
    --rule:#d4d6db;
    --stage:#6d6d6d;
    --white:#ffffff;
    --green:#abd037;
    --purple:#6b449b;
    --teal:#33a6d7;
    --amber:#f7a21b;
  }
  *{box-sizing:border-box;margin:0;padding:0}
  html,body{width:1200px;height:1200px;overflow:hidden}
  body{background:var(--stage);font-family:"Source Sans 3",sans-serif;position:relative}

  .flyer{position:absolute;left:180px;top:56px;width:840px;height:1088px;background:var(--white);overflow:hidden}

  .header-art{position:absolute;left:0;top:0;width:840px;height:440px}

  .tagline{position:absolute;right:70px;top:232px;text-align:right;font-family:"Montserrat",sans-serif;font-weight:700;font-size:17px;line-height:1.25;color:var(--navy);letter-spacing:.3px}
  .tagline-bar{position:absolute;right:52px;top:228px;width:4px;height:48px;background:var(--navy)}

  .brand-badge{position:absolute;left:78px;top:282px;width:170px;height:170px;transform:rotate(45deg);border:9px solid var(--navy);border-radius:22px;background:var(--white);box-shadow:0 6px 14px rgba(0,0,0,.18)}
  .brand{position:absolute;left:78px;top:282px;width:170px;height:170px;display:flex;align-items:center;justify-content:center}
  .brand-name{font-family:"Montserrat",sans-serif;font-weight:700;font-size:24px;color:var(--navy)}

  .services-tab{position:absolute;left:0;top:478px;width:300px;height:48px;background:var(--orange);border-radius:0 26px 26px 0;display:flex;align-items:center;padding-left:42px;font-family:"Montserrat",sans-serif;font-weight:800;font-size:26px;color:var(--white)}

  .values-list{position:absolute;top:548px;list-style:none}
  .values-list.col-a{left:42px}
  .values-list.col-b{left:232px}
  .value{display:flex;align-items:center;gap:12px;height:34px;font-family:"Montserrat",sans-serif;font-weight:500;font-size:17px;color:var(--ink);white-space:nowrap}
  .value-icon{width:24px;height:24px;flex:none}

  .legend-rule{position:absolute;left:42px;top:838px;width:350px;height:1px;background:var(--rule)}
  .legend{position:absolute;left:60px;top:858px;width:340px;display:grid;grid-template-columns:170px 170px;row-gap:22px}
  .legend-item{display:flex;align-items:center;gap:12px;font-size:12px;line-height:1.2;color:var(--muted)}
  .legend-chip{width:30px;height:30px;border-radius:5px;transform:rotate(45deg);flex:none;margin:4px}
  .chip-green{background:var(--green)}
  .chip-purple{background:var(--purple)}
  .chip-teal{background:var(--teal)}
  .chip-amber{background:var(--amber)}

  .who-panel{position:absolute;left:420px;top:410px;width:420px;height:660px;background:var(--navy);padding:28px 34px 0 30px;color:var(--white)}
  .who-title{font-family:"Montserrat",sans-serif;font-weight:700;font-size:25px;letter-spacing:.5px;margin-bottom:16px}
  .who-heading{font-family:"Montserrat",sans-serif;font-weight:800;font-size:19px;color:var(--orange-soft);margin-top:18px;margin-bottom:4px}
  .who-text{font-size:12.2px;line-height:1.42;color:#e9ecf4}

  .footer-band{position:absolute;left:0;bottom:0;width:840px;height:10px;background:var(--orange)}
</style>
</head>
<body>
<main class="flyer">

  <svg class="header-art" viewBox="0 0 840 440">
    <defs>
      <linearGradient id="photoTone" x1="0" y1="0" x2="1" y2="1">
        <stop offset="0" stop-color="#f6d9b8"/>
        <stop offset=".35" stop-color="#e8b88c"/>
        <stop offset=".7" stop-color="#d9cfc8"/>
        <stop offset="1" stop-color="#c9cdd4"/>
      </linearGradient>
    </defs>
    <rect role="img" aria-label="Photo of two people shaking hands over a desk with a laptop in warm window light" x="0" y="0" width="840" height="380" fill="url(#photoTone)"/>
    <path d="M0,440 L0,395 Q380,320 840,300 L840,440 Z" fill="var(--white)"/>
    <path d="M200,392 Q500,300 840,292 L840,346 Q520,340 230,400 Z" fill="var(--navy)"/>
    <path d="M150,420 Q470,360 840,372" fill="none" stroke="#e3e4e8" stroke-width="10"/>
  </svg>

  <div class="tagline">MEDICATION MANAGEMENT AND<br>ADVANCED CLINICAL CONSULTING</div>
  <div class="tagline-bar"></div>

  <div class="brand-badge"></div>
  <div class="brand"><span class="brand-name">Kelvantis</span></div>

  <div class="services-tab">OUR SERVICES</div>

  <ul class="values-list col-a">
    <li class="value"><svg class="value-icon" viewBox="0 0 24 24"><circle cx="12" cy="12" r="10.5" fill="none" stroke="var(--orange)" stroke-width="2"/><path d="M7 16l4-4 3 3 4-6" fill="none" stroke="var(--navy)" stroke-width="1.6"/></svg>Pioneer</li>
    <li class="value"><svg class="value-icon" viewBox="0 0 24 24"><circle cx="12" cy="12" r="10.5" fill="none" stroke="var(--orange)" stroke-width="2"/><circle cx="9" cy="11" r="2.4" fill="var(--navy)"/><circle cx="15" cy="11" r="2.4" fill="var(--navy)"/></svg>Collaborative</li>
    <li class="value"><svg class="value-icon" viewBox="0 0 24 24"><circle cx="12" cy="12" r="10.5" fill="none" stroke="var(--orange)" stroke-width="2"/><path d="M12 17l-4.5-4.5a2.5 2.5 0 0 1 4.5-3a2.5 2.5 0 0 1 4.5 3z" fill="var(--navy)"/></svg>Passionate</li>
    <li class="value"><svg class="value-icon" viewBox="0 0 24 24"><circle cx="12" cy="12" r="10.5" fill="none" stroke="var(--orange)" stroke-width="2"/><circle cx="9.5" cy="12" r="3" fill="none" stroke="var(--navy)" stroke-width="1.6"/><circle cx="14.5" cy="12" r="3" fill="none" stroke="var(--navy)" stroke-width="1.6"/></svg>Integrity</li>
    <li class="value"><svg class="value-icon" viewBox="0 0 24 24"><circle cx="12" cy="12" r="10.5" fill="none" stroke="var(--orange)" stroke-width="2"/><rect x="8" y="8" width="8" height="8" rx="1.5" fill="none" stroke="var(--navy)" stroke-width="1.6"/></svg>Adaptable</li>
    <li class="value"><svg class="value-icon" viewBox="0 0 24 24"><circle cx="12" cy="12" r="10.5" fill="none" stroke="var(--orange)" stroke-width="2"/><path d="M12 6.5l1.7 3.6 3.8.4-2.9 2.6.9 3.8-3.5-2-3.5 2 .9-3.8-2.9-2.6 3.8-.4z" fill="var(--navy)"/></svg>Excellence</li>
    <li class="value"><svg class="value-icon" viewBox="0 0 24 24"><circle cx="12" cy="12" r="10.5" fill="none" stroke="var(--orange)" stroke-width="2"/><path d="M7 12h9M13 8.5l3.5 3.5-3.5 3.5" fill="none" stroke="var(--navy)" stroke-width="1.8"/></svg>Agile</li>
    <li class="value"><svg class="value-icon" viewBox="0 0 24 24"><circle cx="12" cy="12" r="10.5" fill="none" stroke="var(--orange)" stroke-width="2"/><circle cx="12" cy="12" r="3.5" fill="var(--navy)"/></svg>Resourceful</li>
  </ul>

  <ul class="values-list col-b">
    <li class="value"><svg class="value-icon" viewBox="0 0 24 24"><circle cx="12" cy="12" r="10.5" fill="none" stroke="var(--orange)" stroke-width="2"/><circle cx="12" cy="9" r="2.5" fill="var(--navy)"/><path d="M7.5 17a4.5 4.5 0 0 1 9 0z" fill="var(--navy)"/></svg>Entrepreneurial</li>
    <li class="value"><svg class="value-icon" viewBox="0 0 24 24"><circle cx="12" cy="12" r="10.5" fill="none" stroke="var(--orange)" stroke-width="2"/><path d="M12 6v12M8 10h8" stroke="var(--navy)" stroke-width="1.8"/></svg>Respectful</li>
    <li class="value"><svg class="value-icon" viewBox="0 0 24 24"><circle cx="12" cy="12" r="10.5" fill="none" stroke="var(--orange)" stroke-width="2"/><path d="M8 12.5l2.8 2.8L16.5 9" fill="none" stroke="var(--navy)" stroke-width="1.9"/></svg>Solutions</li>
    <li class="value"><svg class="value-icon" viewBox="0 0 24 24"><circle cx="12" cy="12" r="10.5" fill="none" stroke="var(--orange)" stroke-width="2"/><rect x="8.5" y="7" width="7" height="10" rx="1" fill="none" stroke="var(--navy)" stroke-width="1.6"/><path d="M10 10h4M10 12.5h4" stroke="var(--navy)" stroke-width="1.2"/></svg>Accountable</li>
    <li class="value"><svg class="value-icon" viewBox="0 0 24 24"><circle cx="12" cy="12" r="10.5" fill="none" stroke="var(--orange)" stroke-width="2"/><circle cx="12" cy="12" r="5" fill="none" stroke="var(--navy)" stroke-width="1.6"/><circle cx="12" cy="12" r="1.6" fill="var(--navy)"/></svg>Driven</li>
    <li class="value"><svg class="value-icon" viewBox="0 0 24 24"><circle cx="12" cy="12" r="10.5" fill="none" stroke="var(--orange)" stroke-width="2"/><path d="M7 13h4l2 2h4" fill="none" stroke="var(--navy)" stroke-width="1.7"/></svg>Selfless</li>
    <li class="value"><svg class="value-icon" viewBox="0 0 24 24"><circle cx="12" cy="12" r="10.5" fill="none" stroke="var(--orange)" stroke-width="2"/><rect x="7.5" y="8" width="9" height="8.5" rx="1" fill="none" stroke="var(--navy)" stroke-width="1.6"/><path d="M7.5 11h9" stroke="var(--navy)" stroke-width="1.4"/></svg>Disciplined</li>
    <li class="value"><svg class="value-icon" viewBox="0 0 24 24"><circle cx="12" cy="12" r="10.5" fill="none" stroke="var(--orange)" stroke-width="2"/><path d="M8 17v-3M12 17v-6M16 17V8" stroke="var(--navy)" stroke-width="2"/></svg>Growth</li>
  </ul>

  <div class="legend-rule"></div>
  <div class="legend">
    <div class="legend-item"><span class="legend-chip chip-green"></span>Personal and<br>Professional Growth</div>
    <div class="legend-item"><span class="legend-chip chip-purple"></span>Be Your Best Self</div>
    <div class="legend-item"><span class="legend-chip chip-teal"></span>Innovation and<br>Strategy</div>
    <div class="legend-item"><span class="legend-chip chip-amber"></span>Customer<br>Collaboration</div>
  </div>

  <section class="who-panel">
    <h2 class="who-title">WHO WE ARE</h2>

    <h3 class="who-heading">OUR SPIRIT</h3>
    <p class="who-text">Kelvantis was founded to benefit doctors and healthcare providers. We PIONEER technologies and services that are simple, powerful, and fast, which help doctors provide excellent patient care on their own terms. We have an ENTREPRENEURIAL spirit. We are ADAPTABLE, DRIVEN, and innovative. Our focus is broad, reaching horizontally through the healthcare space.</p>

    <h3 class="who-heading">OUR VALUES</h3>
    <p class="who-text">We are COLLABORATIVE and communicate openly, honestly and RESPECTFULLY at all levels. We challenge ourselves to EXCELLENCE, we are SELFLESS, generous, and contribute at our highest capacity.</p>

    <h3 class="who-heading">OUR TEAM</h3>
    <p class="who-text">We are members of a team, and we recognize that our combined efforts make us successful. We welcome challenges and embrace change. We are PASSIONATE about our vision, actively expressing our ideas, and making room for constructive dissent. We are SOLUTIONS oriented, take risks, think differently, and pave our own way as a leader in the market. We are AGILE and fail fast. We are DISCIPLINED to think carefully, plan well, measure our results, and manage the outcomes so that we can succeed in a competitive environment.</p>

    <h3 class="who-heading">OUR COMMITMENT</h3>
    <p class="who-text">We conduct business with INTEGRITY. We are ACCOUNTABLE to one another, our customers, and our partners. We strive to provide affordable prices by being good stewards of our RESOURCES. We are committed to having a GROWTH mindset and doing our best today and doing better tomorrow.</p>
  </section>

  <div class="footer-band"></div>
</main>
</body>
</html>
```